world's hottest chilli salt 7 flavours

I am needing a packaging design for 7 different ones to reflect our range

We are located in Perth OZ. Our chilli salts are new and unique and the world’s hottest ones as we use the world’s hottest chillies. Our product is made from chilli and salts but then other flavours to make them different - one for example is a Smokey one which is very popular and it made from salt, chilli, chipotle, coriander, yellow mustard seeds and garlic.

the colour distinguishes the difference between the different flavours

ingredient list is on the website for each flavour
please view fierymolarz.com at our range of chilli salts

Target Market(s)

Male adults age is from 18 + - target market is Australian market but will be selling overseas as well to the US.

Industry/Entity Type

Product

Requirements
Must have
• must be colour code as examples i have uploaded whether or to view fierymolarsz.com -it it bigger or small i'm not fussed but there needs to be a distinction between the 7 different flavours. Size of label is 95mm x 37mm to work from so very small. The favour the heat (attached) needs to be somewhere on the logo but i would like to see what someone can do with that.
the logo is found with the tongue attached - this is needed and to be quite big if possible – we need the chilli image. It needs to be a good design where our customers and us go WOW.

text of the salts is found on the website.

barcode is needed along the right side. but do not include in the image i will put that on myself

also ingredient list - this is currently not looking any good.

needs to be the "worlds hottest" somewhere
Nice to have
• something clean crisp and elegant like

http://wrapgallerynook.example.com/2009/10/that-bottle.html

** this is what we would like http://img.pixhoardly.example.com/_9KqWmTzR2LP/XbNa-7QsdHo/ZZZZZZZZKL2/pTe4RRvWYCA/s1600/QLMX+tiles.jpg
clean crisp and
Should not have
• too many fonts

```html
<!DOCTYPE html>
<html lang="en">
<head>
<meta charset="utf-8">
<title>World's Hottest Chilli Spice – Label</title>
<link href="https://fonts.googleapis.com/css2?family=Arimo:wght@400;700&family=Alfa+Slab+One&display=swap" rel="stylesheet">
<style>
  :root {
    --page: #ffffff;
    --label-bg: #231f20;
    --panel-bg: #3d3b3c;
    --chilli-red: #ed1c24;
    --text-light: #ffffff;
    --text-soft: #e6e6e6;
    --character-dark: #8e1116;
    --character-mid: #d9232a;
    --flame: #f7b01e;
  }
  * { margin: 0; padding: 0; box-sizing: border-box; }
  html, body { width: 1200px; height: 900px; overflow: hidden; background: var(--page); }
  body { position: relative; font-family: "Arimo", Arial, sans-serif; }

  .label {
    position: absolute; left: 26px; top: 228px; width: 1122px; height: 434px;
    background: var(--label-bg); overflow: hidden;
  }
  .flavour-band {
    position: absolute; left: 0; top: 162px; width: 100%; height: 70px;
    background: var(--chilli-red);
  }
  .eyebrow {
    position: absolute; left: 36px; top: 24px;
    font-weight: 700; font-size: 31px; color: var(--text-light); letter-spacing: 0.2px;
  }
  .product-name {
    position: absolute; left: 32px; top: 52px;
    font-family: "Alfa Slab One", Georgia, serif; font-size: 72px; line-height: 1;
    color: var(--chilli-red); letter-spacing: 2px;
  }
  .flavour-name {
    position: absolute; left: 36px; top: 171px;
    font-weight: 700; font-size: 21px; line-height: 29px; color: var(--text-light);
  }
  .description {
    position: absolute; left: 36px; top: 250px;
    font-size: 17.5px; line-height: 25px; color: var(--text-soft);
  }
  .heat-row {
    position: absolute; left: 36px; top: 340px; height: 60px;
    display: flex; align-items: center;
  }
  .heat-markers { display: flex; gap: 4px; margin-right: 12px; }
  .heat-level { font-size: 25px; color: var(--text-light); }
  .divider { width: 2px; height: 42px; background: var(--text-light); margin: 0 16px 0 18px; }
  .website { font-weight: 700; font-size: 21px; color: var(--text-light); }

  .mascot {
    position: absolute; left: 628px; top: 12px; width: 240px; height: 400px;
    border-radius: 45% 45% 40% 40%;
    background: radial-gradient(ellipse at 45% 40%, var(--character-mid) 0%, var(--character-dark) 65%, transparent 72%),
                radial-gradient(ellipse at 75% 30%, var(--flame) 0%, transparent 40%);
  }
  .mascot-name {
    position: absolute; left: 628px; top: 290px; width: 210px; height: 80px;
    background: var(--text-light); display: flex; align-items: center; justify-content: center;
    font-weight: 700; font-size: 24px; color: var(--chilli-red); text-transform: uppercase;
  }

  .info-panel {
    position: absolute; left: 902px; top: 28px; width: 192px; height: 366px;
    background: var(--panel-bg); padding: 16px 14px;
  }
  .panel-heading { font-size: 16px; color: var(--chilli-red); text-transform: uppercase; line-height: 18px; }
  .panel-text { font-size: 14.5px; line-height: 17px; color: var(--text-soft); margin-top: 4px; }
  .origin { position: absolute; left: 14px; top: 246px; }
  .net-weight {
    position: absolute; left: 14px; top: 325px;
    font-weight: 700; font-size: 24px; color: var(--chilli-red);
  }
</style>
</head>
<body>
  <main class="label">
    <div class="flavour-band"></div>

    <p class="eyebrow">WORLD’S HOTTEST</p>
    <h1 class="product-name">CHILLI SPICE</h1>

    <p class="flavour-name">Bhut Jolokia Chilli (World’s Hottest Chilli)<br>&amp; Pink Himilayan Rock Salt</p>

    <p class="description">An excellent all-round salt to enhance the flavour<br>of any meal. Adds a little salt and lots of zing! No MSG.</p>

    <div class="heat-row">
      <svg class="heat-markers" width="104" height="56" viewBox="0 0 104 56" aria-hidden="true">
        <g fill="#ed1c24">
          <path d="M14 8 C4 14 2 30 10 44 C14 52 22 54 24 48 C18 40 16 26 22 14 Z"/>
          <path d="M50 8 C40 14 38 30 46 44 C50 52 58 54 60 48 C54 40 52 26 58 14 Z"/>
          <path d="M86 8 C76 14 74 30 82 44 C86 52 94 54 96 48 C90 40 88 26 94 14 Z"/>
        </g>
        <g fill="#3a7d2c">
          <rect x="15" y="2" width="6" height="8" rx="2"/>
          <rect x="51" y="2" width="6" height="8" rx="2"/>
          <rect x="87" y="2" width="6" height="8" rx="2"/>
        </g>
      </svg>
      <span class="heat-level">VERY HOT</span>
      <span class="divider"></span>
      <span class="website">fierymolarsz.com</span>
    </div>

    <div class="mascot" role="img" aria-label="Illustrated grinning red chilli mascot with a yellow flame"></div>
    <div class="mascot-name">Savour the Blaze</div>

    <aside class="info-panel">
      <h2 class="panel-heading">Ingredients</h2>
      <p class="panel-text">Bhut Jolokia Chilli,<br>Pink Himilayan<br>Rock Salt.</p>

      <div class="origin">
        <h2 class="panel-heading">Made in WA</h2>
        <p class="panel-text" style="margin-top:0">PO BOX 472<br>Redgum Vale 6990</p>
      </div>

      <p class="net-weight">100g</p>
    </aside>
  </main>
</body>
</html>
```